Solar appointment reminder card

We are looking for a new design for our appointment reminder card since we have changed our logo. The card should have the new logo along with space for the employee to hand write the customers appointment date, time, the employees name and phone number.
I've uploaded what our old basic appointment card looked like and our new logo.

The cards should be in a standard business card size and could be horizontal or vertical.

```html
<!DOCTYPE html>
<html lang="en">
<head>
<meta charset="utf-8">
<title>Brightline Solar – Appointment Card</title>
<link href="https://fonts.googleapis.com/css2?family=Lato:wght@400;700;900&family=Roboto+Condensed:wght@400&display=swap" rel="stylesheet">
<style>
  :root {
    --backdrop: #afafaf;
    --card: #ffffff;
    --orange: #f7941d;
    --sun: #fdc52f;
    --ink: #231f20;
  }
  * { box-sizing: border-box; margin: 0; padding: 0; }
  html, body {
    width: 1200px; height: 1200px; overflow: hidden;
    background: var(--backdrop);
  }
  .card {
    position: absolute;
    left: 176px; top: 279px;
    width: 847px; height: 487px;
    background: var(--card);
    font-family: "Lato", sans-serif;
    color: var(--ink);
  }
  .brand {
    position: absolute;
    left: 40px; top: 92px;
    display: flex; align-items: center; gap: 16px;
  }
  .brand-dot {
    width: 64px; height: 64px; border-radius: 50%;
    background: var(--sun);
  }
  .brand-name {
    font-weight: 900;
    font-size: 44px;
    color: var(--orange);
    letter-spacing: -0.5px;
  }
  .card-title {
    position: absolute;
    right: 40px; top: 169px;
    font-weight: 900;
    font-size: 26px;
    color: var(--orange);
    letter-spacing: -0.3px;
  }
  .form {
    position: absolute;
    left: 134px; right: 39px; top: 276px;
  }
  .row { display: flex; align-items: baseline; }
  .field { display: flex; align-items: baseline; }
  .label { white-space: nowrap; margin-right: 4px; }
  .fill-line {
    flex: 1;
    border-bottom: 2px dotted var(--ink);
    height: 1px;
  }
  .row-contact { font-size: 22px; }
  .row-contact .field-name { flex: 0 0 378px; }
  .row-contact .field-phone { flex: 1; margin-left: 12px; }
  .row-days {
    margin-top: 36px;
    justify-content: space-between;
    font-size: 22px;
  }
  .check { display: flex; align-items: center; gap: 10px; }
  .box {
    width: 19px; height: 19px;
    border: 2px solid var(--ink);
  }
  .row-when { margin-top: 36px; font-size: 19px; }
  .row-when .field-date { flex: 0 0 254px; }
  .row-when .field-time { flex: 0 0 244px; margin-left: 24px; }
  .meridiem { display: flex; gap: 14px; margin-left: auto; font-size: 18px; }
  .meridiem .check { gap: 9px; }
  .meridiem .box { width: 15px; height: 15px; }
  .notice {
    margin-top: 16px;
    font-family: "Roboto Condensed", sans-serif;
    font-size: 23px;
    color: var(--orange);
    letter-spacing: -0.2px;
    white-space: nowrap;
  }
</style>
</head>
<body>
  <div class="card">
    <div class="brand">
      <span class="brand-dot"></span>
      <span class="brand-name">Brightline Solar</span>
    </div>
    <h1 class="card-title">NEXT APPOINTMENT</h1>

    <div class="form">
      <div class="row row-contact">
        <div class="field field-name"><span class="label">Name:</span><span class="fill-line"></span></div>
        <div class="field field-phone"><span class="label">Phone:</span><span class="fill-line"></span></div>
      </div>

      <div class="row row-days">
        <span class="check"><span class="box"></span>MON</span>
        <span class="check"><span class="box"></span>TUES</span>
        <span class="check"><span class="box"></span>WED</span>
        <span class="check"><span class="box"></span>THUR</span>
        <span class="check"><span class="box"></span>FRI</span>
      </div>

      <div class="row row-when">
        <div class="field field-date"><span class="label">Date:</span><span class="fill-line"></span></div>
        <div class="field field-time"><span class="label">Time:</span><span class="fill-line"></span></div>
        <div class="meridiem">
          <span class="check"><span class="box"></span>AM</span>
          <span class="check"><span class="box"></span>PM</span>
        </div>
      </div>

      <p class="notice">If you are unable to keep your appointment, please call us as soon as possible</p>
    </div>
  </div>
</body>
</html>
```